Business Card for Pottery and Jewellery Designer

A new business card design is needed to accompany a newly launching pottery and jewellery website. The company logo has been attached for use. The company is called Glazewick Studio. For a sense of the vibe please see the website (it is currently under construction but this way you'll get a feel for the style) www.GlazewickStudio.com

The website font is Pontano Sans for the body of the text with Overlock for headers.

The overall look should be clean and elegant. The back side can have just the logo. The front side should have a smaller logo and the following details displayed:

Glazewick Studio
Designer: Hollis Marrow
Phone: xxx.xxx.xxxx
Email: Designer@GlazewickStudio.com

The structure of displaying this is completely up to you. Different layouts and creative methods of displaying contact info are welcome as long as it stays clean/uncluttered.

No product photographs are to be included in the design as the catalogue changes quickly.

Colour preferences lean towards elegant and understated (charcoal grey, dark navy blue etc.)

Please let me know if you have any further questions or further details required.

Target Market(s)

Target market is 30+ year old women

Industry/Entity Type

Construction

Colors
ffffff
1b1b1b
474747
d9d9d9
fafafa
0355a3

Requirements
Must have
• The submissions so far have looked very typical and don't stand out right now. They're also all in navy with very little variation. I'm looking for something that stands out a it more while still being clean-looking.
Nice to have
• I've attached a few design samples and an idea for a backdrop. It would be great to see some designs in black, white, and grey with only a hint of color.
Should not have
• Product Images

```html
<!DOCTYPE html>
<html lang="en">
<head>
<meta charset="utf-8">
<title>Glazewick Studio – Business Card</title>
<link href="https://fonts.googleapis.com/css2?family=Play:wght@400;700&display=swap" rel="stylesheet">
<style>
  :root {
    --backdrop: #e6e6e6;
    --charcoal: #1b1b1b;
    --graphite: #474747;
    --frame-grey: #d9d9d9;
    --paper: #ffffff;
    --paper-soft: #fafafa;
    --ink: #1b1b1b;
    --ink-soft: #474747;
    --accent: #0355a3;
    --rule: #ffffff;
  }
  * { box-sizing: border-box; margin: 0; padding: 0; }
  html, body { width: 1200px; height: 786px; overflow: hidden; }
  body {
    background: var(--backdrop);
    font-family: "Play", "Segoe UI", sans-serif;
    position: relative;
  }
  .card {
    position: absolute;
    top: 244px;
    width: 520px;
    height: 298px;
    box-shadow: 0 6px 18px rgba(0,0,0,.16);
  }

  /* Back side */
  .card--back { left: 50px; background: var(--charcoal); padding: 16px; }
  .card--back .card__face {
    width: 100%; height: 100%;
    background: var(--paper);
    display: flex; align-items: center; justify-content: center; gap: 14px;
    position: relative;
  }
  .card--back .card__face::after {
    content: "";
    position: absolute; left: 50%; bottom: 86px;
    width: 48px; height: 2px; margin-left: -24px;
    background: var(--accent);
  }
  .brand__mark {
    width: 34px; height: 34px; border-radius: 50%;
    background: var(--accent); flex: none;
  }
  .brand__name {
    color: var(--charcoal);
    font-weight: 400;
    letter-spacing: 3px;
    text-transform: uppercase;
    white-space: nowrap;
  }
  .card--back .brand__name { font-size: 26px; }

  /* Front side */
  .card--front { left: 630px; background: var(--frame-grey); padding: 14px; }
  .card--front .card__face {
    width: 100%; height: 100%;
    background: var(--paper);
    position: relative;
    overflow: hidden;
  }
  .front__brand {
    position: absolute; left: 22px; top: 28px;
    display: flex; align-items: center; gap: 10px;
  }
  .front__brand .brand__mark { width: 26px; height: 26px; }
  .front__brand .brand__name { font-size: 15px; letter-spacing: 2px; }

  .holder {
    position: absolute; right: 20px; top: 76px;
    text-align: right; color: var(--ink);
    text-transform: uppercase;
  }
  .holder__name { font-size: 15px; letter-spacing: 1px; }
  .holder__role { font-size: 11px; letter-spacing: 1px; color: var(--accent); }

  .contact-grid {
    position: absolute; left: 0; right: 0; bottom: 0;
    display: grid;
    grid-template-columns: repeat(3, 1fr);
    align-items: end;
  }
  .contact {
    display: flex; flex-direction: column;
    border-left: 2px solid var(--rule);
  }
  .contact:first-child { border-left: none; }
  .contact__head {
    height: 34px;
    background: var(--graphite);
    border-bottom: 2px solid var(--accent);
    display: flex; align-items: center; justify-content: center;
  }
  .contact__body {
    background: var(--charcoal);
    color: var(--paper-soft);
    font-size: 10.5px;
    letter-spacing: .6px;
    line-height: 1.45;
    padding: 0 12px;
    display: flex; flex-direction: column; justify-content: center;
    white-space: nowrap;
  }
  .contact--phone .contact__body { height: 118px; align-items: center; }
  .contact--web .contact__body { height: 80px; }
  .contact--place .contact__body { height: 70px; }
  .icon { width: 20px; height: 20px; }
</style>
</head>
<body>

  <section class="card card--back" aria-label="Business card, back">
    <div class="card__face">
      <span class="brand__mark"></span>
      <span class="brand__name">Glazewick Studio</span>
    </div>
  </section>

  <section class="card card--front" aria-label="Business card, front">
    <div class="card__face">
      <div class="front__brand">
        <span class="brand__mark"></span>
        <span class="brand__name">Glazewick Studio</span>
      </div>

      <div class="holder">
        <p class="holder__name">Hollis Marrow</p>
        <p class="holder__role">Designer</p>
      </div>

      <div class="contact-grid">
        <div class="contact contact--phone">
          <div class="contact__head">
            <svg class="icon" viewBox="0 0 20 20" fill="none" stroke="#fff" stroke-width="1.4">
              <circle cx="10" cy="10" r="8.5"/>
              <path d="M7.2 5.8l1.3 1.9-.9 1.1c.5 1.1 1.4 2 2.5 2.5l1.1-.9 1.9 1.3-.8 1.6c-2.9-.3-5.6-3-5.9-5.9z" fill="#fff" stroke="none"/>
            </svg>
          </div>
          <div class="contact__body">
            <p>014 262 7315</p>
            <p>014 262 7315</p>
          </div>
        </div>

        <div class="contact contact--web">
          <div class="contact__head">
            <svg class="icon" viewBox="0 0 20 20" fill="none" stroke="#fff" stroke-width="1.2">
              <circle cx="10" cy="10" r="8.5"/>
              <circle cx="10" cy="10" r="5"/>
              <ellipse cx="10" cy="10" rx="2.2" ry="5"/>
              <path d="M5 10h10"/>
            </svg>
          </div>
          <div class="contact__body">
            <p>hollis@glazewick.com</p>
            <p>www.GlazewickStudio.com</p>
          </div>
        </div>

        <div class="contact contact--place">
          <div class="contact__head">
            <svg class="icon" viewBox="0 0 20 20" fill="none" stroke="#fff" stroke-width="1.4">
              <circle cx="10" cy="10" r="8.5"/>
              <path d="M10 15s-3.2-3.6-3.2-6a3.2 3.2 0 0 1 6.4 0c0 2.4-3.2 6-3.2 6z" fill="#fff" stroke="none"/>
              <circle cx="10" cy="9" r="1.1" fill="#474747" stroke="none"/>
            </svg>
          </div>
          <div class="contact__body">
            <p>041, 9th floor, Kiln Row</p>
            <p>Alder Road EVT</p>
          </div>
        </div>
      </div>
    </div>
  </section>

</body>
</html>
```